Animal Eye Clinic needs a Business card

We are a new veterinary ophthalmology practice (Tessaly Animal Eye Care) and we need a business card designed. We only see animal eyes - we are not a regular veterinary clinic. We already have a logo. We are looking for a professional, good looking business card to hand out to our clients. We are looking for something simple but professional and contemporary. Our logo is likely the only picture/graphic that needs to be on the card.
Updates

Contact Information for Business Card

Marisol Dunkley, BSc, DVM, MSc, DipACVO
Veterinary Ophthalmologist

Phone: 250.418.3097
Email: tessalyanimaleyecare@mailbrook.net
Website: tessalyanimaleyecare.net
Address: 1840 Pellworth Rd
Kelowna, BC, V4T 8M3

Colors

Designer to choose colors to be used in the design.

Requirements
Must have
• Our logo (attached)

```html
<!DOCTYPE html>
<html lang="en">
<head>
<meta charset="utf-8">
<title>Tessaly Animal Eye Care – Business Card</title>
<link rel="stylesheet" href="https://fonts.googleapis.com/css2?family=Arimo:wght@400&family=Tinos&display=swap">
<style>
  :root {
    --sky-light: #a6f4f9;
    --stripe-1: #3fc6ec;
    --stripe-2: #63d7f1;
    --stripe-3: #8be5f5;
    --teal: #3cbfa6;
    --ink: #1c1c1c;
    --white: #ffffff;
  }
  * { margin: 0; padding: 0; box-sizing: border-box; }
  html, body { width: 1200px; height: 720px; overflow: hidden; background: #ffffff; }
  .card {
    position: relative;
    width: 1200px;
    height: 720px;
    overflow: hidden;
    font-family: "Tinos", "Times New Roman", serif;
    color: var(--ink);
  }
  .card-art { position: absolute; inset: 0; width: 1200px; height: 720px; }
  .brand {
    position: absolute;
    left: 0; top: 51px;
    width: 610px; height: 150px;
    background: var(--white);
    display: flex;
    align-items: center;
    padding-left: 34px;
    gap: 26px;
  }
  .brand-dot {
    width: 96px; height: 96px;
    border-radius: 50%;
    background: var(--teal);
    flex: none;
  }
  .brand-name {
    font-family: "Tinos", "Times New Roman", serif;
    font-weight: 400;
    font-size: 38px;
    color: var(--ink);
    white-space: nowrap;
  }
  .person { position: absolute; left: 40px; top: 355px; }
  .person-name {
    font-family: "Arimo", Arial, sans-serif;
    font-size: 32px;
    font-weight: 400;
    letter-spacing: 0.5px;
  }
  .person-credentials { font-size: 24px; margin-top: 8px; }
  .person-title { font-size: 27px; margin-top: 4px; margin-left: -2px; }
  .contact {
    position: absolute;
    left: 14px; top: 514px;
    border-left: 1.5px solid var(--ink);
    padding-left: 3px;
    font-size: 25px;
    line-height: 39.5px;
    list-style: none;
  }
</style>
</head>
<body>
<main class="card">
  <svg class="card-art" viewBox="0 0 1125 675" preserveAspectRatio="none">
    <defs>
      <linearGradient id="sky" x1="0" y1="0" x2="1" y2="1">
        <stop offset="0" stop-color="#8cf0f8"/>
        <stop offset="1" stop-color="#a9f5f9"/>
      </linearGradient>
      <linearGradient id="fur" x1="0" y1="0" x2="1" y2="0">
        <stop offset="0" stop-color="#8f5f3b"/>
        <stop offset="0.45" stop-color="#c89a6e"/>
        <stop offset="0.8" stop-color="#ece7e1"/>
        <stop offset="1" stop-color="#f4f2ef"/>
      </linearGradient>
      <filter id="soft-shadow" x="-20%" y="-20%" width="140%" height="140%">
        <feDropShadow dx="0" dy="0" stdDeviation="8" flood-color="#1a6f80" flood-opacity="0.35"/>
      </filter>
    </defs>
    <rect class="sky" width="1125" height="675" fill="url(#sky)"/>
    <polygon class="stripe" points="560,0 690,0 510,330 630,675 500,675 420,330" fill="var(--stripe-3)" filter="url(#soft-shadow)"/>
    <polygon class="stripe" points="690,0 760,0 575,330 700,675 630,675 510,330" fill="var(--stripe-2)" filter="url(#soft-shadow)"/>
    <polygon class="stripe" points="760,0 835,0 645,330 770,675 700,675 575,330" fill="var(--stripe-1)" filter="url(#soft-shadow)"/>
    <g role="img" aria-label="Close-up photograph of a beagle's face and eye">
      <polygon points="835,0 1125,0 1125,675 770,675 645,330" fill="url(#fur)" filter="url(#soft-shadow)"/>
    </g>
    <circle class="info-disc" cx="190" cy="650" r="365" fill="var(--white)" filter="url(#soft-shadow)"/>
  </svg>

  <header class="brand">
    <span class="brand-dot" aria-hidden="true"></span>
    <h1 class="brand-name">Tessaly Animal Eye Care</h1>
  </header>

  <section class="person">
    <p class="person-name">Marisol Dunkley,</p>
    <p class="person-credentials">BSc, DVM, MSc, DipACVO</p>
    <p class="person-title">Veterinary Ophthalmologist</p>
  </section>

  <ul class="contact">
    <li class="contact-phone">Phone: 250.418.3097</li>
    <li class="contact-email">Email:tessalyanimaleyecare@mailbrook.net</li>
    <li class="contact-web">Website: tessalyanimaleyecare.net</li>
    <li class="contact-address">Address: 1840 Pellworth Rd</li>
    <li class="contact-city">Kelowna, BC, V4T 8M3</li>
  </ul>
</main>
</body>
</html>
```